【表紙要素】

■書籍タイトル
頼りない課長だった僕が十五期続いた欠損の倉庫業者を再生させた方法

■サブタイトル
町工場のための統率術入門

■キャッチコピー1
「灯台守ステップ術」で部下はあなたについてくる

■キャッチコピー2
特別セミナー動画(無料プレゼント)付き
「粗利が倍増する。倉庫業者が今日から使える5つの収益改善フレーム」

■著者
桐島のぶお

■肩書
物流マーケティングコンサルタント
次世代リーダー育成コンサルタント

■書籍の内容
総合物流会社から赤字続きの関連小会社へ出向となった著者が、会社を立て直す中で学んだリーダーシップ論がテーマになっています。原稿も添付いたします。

■ターゲット
運輸会社の経営者・部課長をターゲットとしています。

■デザイン要望
・イラストを入れるとすると、売上が右肩上がりになっているグラフなどのイメージかなと思いってます。もちろん、その他に良いアイデアがあれば採用したいと思います。
・イラストが入っても、文字だけでも、どちらでも構いません。できれば両方のパターンを比較して決めたいと思います。
・タイトルに関しては、「頼りない課長だった僕が」は小さく、「赤字」「黒字化」は目立つようにお願いします。

本の本文の内容が、あまり堅苦しくない、おもしろおかしい要素が含まれていますので、表紙も明るくてポップな感じが気に入りました。
ただし、誠に申し訳ないのですが、急遽、電子書籍のタイトルを変更することになりました。また、表紙の文字数も減らすことにしました。
したがいまして、今回のコンペとは別に、本日中に再発注をかけます。
何卒、ご理解いただき、再度コンペへのご参加をお願いいたします。

ご提案いただき、ありがとうございました。また、原稿を読んで頂き、内容を踏まえた上でデザインを考えていただき、大変感謝しています。
いろいろと考えた結果、急遽、電子書籍のタイトルを変更することになりました。今回のコンペとは別に、再度依頼をかけますので、またコンペにご参加いただけますようお願いいたします。

```html
<!DOCTYPE html>
<html lang="ja">
<head>
<meta charset="utf-8">
<title>頼りない課長だった僕が十五期続いた欠損の倉庫業者を再生させた方法</title>
<link href="https://fonts.googleapis.com/css2?family=Noto+Sans+JP:wght@400;500;700;900&display=swap" rel="stylesheet">
<style>
  :root {
    --ink: #1a1a1a;
    --paper: #f4f4f2;
    --red: #d7141e;
    --band-grey: #8c8c8c;
    --box-dark: #3a3a3a;
    --bar-blue: #2f8fd6;
    --bar-green: #3fb34a;
    --bar-yellow: #f2d21a;
    --bar-orange: #f08a1c;
    --bar-red: #e0352b;
    --bar-grey: #7a7a7a;
  }
  html, body { margin: 0; padding: 0; overflow: hidden; }
  body { width: 845px; height: 1200px; background: #fff; }
  .cover {
    position: relative; width: 845px; height: 1200px; overflow: hidden;
    background: linear-gradient(180deg, #ffffff 0%, var(--paper) 60%, #ffffff 100%);
    font-family: "Noto Sans JP", sans-serif; color: var(--ink);
  }
  .chart { position: absolute; left: 0; top: 0; }
  .hero-figure {
    position: absolute; left: 705px; top: 80px; width: 70px; height: 318px;
    background: linear-gradient(180deg, #3b3b3b, #161616);
    border-radius: 30px 30px 6px 6px;
  }
  .title-lead {
    position: absolute; left: 120px; top: 40px; font-size: 30px; font-weight: 700;
    font-style: italic; letter-spacing: 1px; white-space: nowrap; line-height: 1.3;
  }
  .title-lead .dots { text-emphasis: filled dot var(--red); -webkit-text-emphasis: filled dot var(--red); text-emphasis-position: over; }
  .title-mid {
    position: absolute; left: 118px; top: 84px; font-size: 32px; font-weight: 900; white-space: nowrap; line-height: 1.3;
  }
  .title-mid .accent { color: var(--red); font-size: 50px; }
  .title-main {
    position: absolute; left: 110px; top: 152px; font-size: 130px; font-weight: 900; line-height: 1; letter-spacing: 6px;
  }
  .title-sub {
    position: absolute; left: 118px; top: 286px; font-size: 74px; font-weight: 900; line-height: 1; white-space: nowrap;
  }
  .subtitle-band {
    position: absolute; left: 110px; top: 392px; width: 570px; height: 48px;
    background: var(--band-grey); color: #fff; font-size: 26px; font-weight: 500;
    line-height: 48px; padding-left: 24px; box-sizing: border-box; letter-spacing: 2px; white-space: nowrap;
  }
  .author { position: absolute; left: 168px; top: 470px; }
  .author-role { font-size: 13px; font-weight: 500; line-height: 20px; }
  .author-name { font-size: 40px; font-weight: 900; margin-top: 4px; letter-spacing: 3px; line-height: 1.3; }
  .author-roman { font-size: 15px; font-weight: 700; letter-spacing: 1px; }
  .catch {
    position: absolute; left: 100px; top: 885px; width: 700px; height: 140px;
    background: #fff;
  }
  .catch-row { position: absolute; left: 14px; top: 16px; display: flex; align-items: flex-end; }
  .catch-method {
    border: 3px solid var(--ink); padding: 2px 12px; font-size: 44px; font-weight: 900;
    white-space: nowrap; letter-spacing: 1px; line-height: 1.35;
  }
  .catch-de { font-size: 36px; font-weight: 900; margin-left: 8px; line-height: 1.2; }
  .catch-line { position: absolute; left: 120px; top: 94px; font-size: 30px; font-weight: 900; white-space: nowrap; line-height: 1.2; }
  .bonus {
    position: absolute; left: 228px; top: 1070px; width: 520px; height: 118px;
    background: var(--box-dark); color: #fff; text-align: center; box-sizing: border-box; padding-top: 14px;
  }
  .bonus-tag {
    position: absolute; left: 16px; top: -16px; background: #fff; color: var(--ink);
    border: 2px solid var(--box-dark); font-size: 15px; font-weight: 700; padding: 2px 10px; line-height: 1.3; white-space: nowrap;
  }
  .bonus-lead { font-size: 20px; font-weight: 700; line-height: 1.2; }
  .bonus-main { font-size: 32px; font-weight: 900; line-height: 1.2; }
  .bonus-tail { font-size: 26px; font-weight: 700; line-height: 1.2; }
</style>
</head>
<body>
<div class="cover">
  <svg class="chart" width="845" height="1200" viewBox="0 0 845 1200" aria-hidden="true">
    <defs>
      <linearGradient id="fade" x1="0" y1="0" x2="0" y2="1">
        <stop offset="0" stop-color="#fff" stop-opacity="0"/>
        <stop offset="1" stop-color="#fff" stop-opacity="1"/>
      </linearGradient>
    </defs>
    <polygon points="170,780 217,740 265,780 265,900 170,900" fill="var(--bar-blue)"/>
    <polygon points="282,715 331,675 380,715 380,900 282,900" fill="var(--bar-green)"/>
    <polygon points="395,620 445,580 495,620 495,900 395,900" fill="var(--bar-yellow)"/>
    <polygon points="508,580 556,540 605,580 605,900 508,900" fill="var(--bar-orange)"/>
    <polygon points="600,490 645,450 690,490 690,900 600,900" fill="var(--bar-red)"/>
    <rect x="690" y="398" width="100" height="502" fill="var(--bar-grey)"/>
    <rect x="150" y="800" width="660" height="100" fill="url(#fade)"/>
  </svg>
  <div class="hero-figure" role="img" aria-label="頂上の棒グラフに立つスーツ姿のビジネスマンの写真"></div>

  <div class="title-lead"><span class="dots">頼りない課長</span>だった僕が</div>
  <div class="title-mid">十五期続いた<span class="accent">欠損</span>の倉庫業者を</div>
  <div class="title-main">再生</div>
  <div class="title-sub">させた方法</div>
  <div class="subtitle-band">町工場のための統率術入門</div>

  <div class="author">
    <div class="author-role">物流マーケティングコンサルタント</div>
    <div class="author-role">次世代リーダー育成コンサルタント</div>
    <div class="author-name">桐島のぶお</div>
    <div class="author-roman">NOBUO KIRISHIMA</div>
  </div>

  <div class="catch">
    <div class="catch-row">
      <div class="catch-method">「灯台守ステップ術」</div>
      <div class="catch-de">で</div>
    </div>
    <div class="catch-line">部下はあなたについてくる</div>
  </div>

  <div class="bonus">
    <div class="bonus-tag">特別セミナー動画(無料プレゼント)付き</div>
    <div class="bonus-lead">粗利が倍増する。</div>
    <div class="bonus-main">倉庫業者が今日から使える</div>
    <div class="bonus-tail">5つの収益改善フレーム</div>
  </div>
</div>
</body>
</html>
```